Need Eye Catching For Sale By Owner Signs

In need of a Eye Catching For Sale By Owner Sign design. I plan on using the sign to market buildings and raw land that I own. The design should be able to scale to different rectangular dimensions for example a yard stake sign or a large 4' x 6' sign to be tacked to plywood. The design should have a dead space near the bottom that I can insert more detail information into at a later time.

The main tag line "For Sale By Owner" and the contact number "319-562-4097" needs to be easily be read from a distance.

```html
<!DOCTYPE html>
<html lang="en">
<head>
<meta charset="UTF-8">
<title>For Sale By Owner Sign</title>
<link href="https://fonts.googleapis.com/css2?family=Bebas+Neue&family=Archivo+Black&display=swap" rel="stylesheet">
<style>
  :root {
    --sign-red: #be1e2d;
    --sign-white: #ffffff;
  }
  html, body {
    margin: 0;
    padding: 0;
    width: 1200px;
    height: 816px;
    overflow: hidden;
    background: var(--sign-white);
  }
  .sign {
    display: block;
    width: 1200px;
    height: 816px;
  }
  .header-band { fill: var(--sign-red); }
  .frame-upper { fill: none; stroke: var(--sign-white); stroke-width: 4; }
  .frame-lower { fill: none; stroke: var(--sign-red); stroke-width: 4; }
  .headline {
    font-family: "Bebas Neue", "Oswald", sans-serif;
    font-size: 343px;
    fill: var(--sign-white);
  }
  .subline {
    font-family: "Archivo Black", "Arial Black", sans-serif;
    font-size: 126px;
    fill: var(--sign-white);
  }
  .phone {
    font-family: "Archivo Black", "Arial Black", sans-serif;
    font-size: 133px;
    fill: var(--sign-red);
  }
  .house-icon { fill: var(--sign-red); }
  .house-roof { fill: none; stroke: var(--sign-red); stroke-width: 10; stroke-linejoin: miter; }
</style>
</head>
<body>
<svg class="sign" viewBox="0 0 1200 816" xmlns="http://www.w3.org/2000/svg">
  <defs>
    <clipPath id="upper-area"><rect x="0" y="0" width="1200" height="484"/></clipPath>
    <clipPath id="lower-area"><rect x="0" y="484" width="1200" height="332"/></clipPath>
  </defs>

  <rect class="header-band" x="0" y="0" width="1200" height="484"/>

  <rect class="frame-upper" x="48" y="48" width="1110" height="726" clip-path="url(#upper-area)"/>
  <rect class="frame-lower" x="48" y="48" width="1110" height="726" clip-path="url(#lower-area)"/>

  <text class="headline" x="182" y="346" textLength="826" lengthAdjust="spacingAndGlyphs">FOR SALE</text>
  <text class="subline" x="244" y="465" textLength="712" lengthAdjust="spacingAndGlyphs">BY OWNER</text>
  <text class="phone" x="150" y="599" textLength="950" lengthAdjust="spacingAndGlyphs">319.562.4097</text>

  <g class="house">
    <polyline class="house-roof" points="983,687 1046,636 1109,687"/>
    <rect class="house-icon" x="1085" y="628" width="14" height="34"/>
    <path class="house-icon" d="M1000,686 L1046,650 L1092,686 L1092,739 L1058,739 L1058,704 L1034,704 L1034,739 L1000,739 Z"/>
  </g>
</svg>
</body>
</html>
```